Local Mortgage Broker requires DL Flyer

I Require DL sized design for local mortgage broker. Content that will go on the flyer is attached along with the logo.
Looking for a bright & catchy design with that little OOMPH.....on the creative side.
Am looking for a responsive campaign with this style of marketing. The main message is that "We may be able to save thousands of dollars for you, just give us a chance to review your mortgages"

Target Market(s)

All home owners with a mortgage or eople looking to buy their first home.

Industry/Entity Type

Marketing

```html
<!DOCTYPE html>
<html lang="en">
<head>
<meta charset="utf-8">
<title>KeyHaven Finance – DL Flyer</title>
<link href="https://fonts.googleapis.com/css2?family=Fira+Sans:wght@400;600;700;800&display=swap" rel="stylesheet">
<style>
  :root {
    --yellow: #fff200;
    --navy: #2a2660;
    --ink: #2b2862;
    --white: #ffffff;
    --photo-light: #d9d4d0;
    --photo-mid: #b9aaa2;
    --photo-warm: #d7b39c;
  }
  * { margin: 0; padding: 0; box-sizing: border-box; }
  html, body { width: 1200px; height: 2544px; overflow: hidden; background: var(--white); }
  body { font-family: "Fira Sans", Arial, sans-serif; }

  .flyer { position: relative; width: 1200px; height: 2544px; overflow: hidden; background: var(--navy); }

  .header-band {
    position: absolute; left: 0; top: 0; width: 1200px; height: 329px;
    background: var(--yellow);
    display: flex; flex-direction: column; justify-content: center; align-items: center;
  }
  .headline {
    color: var(--ink); font-weight: 800; font-size: 92px; line-height: 122px;
    text-align: center; letter-spacing: 1px; text-transform: uppercase;
  }

  .hero-photo {
    position: absolute; left: 0; top: 329px; width: 1200px; height: 858px;
    background:
      radial-gradient(ellipse 420px 360px at 560px 480px, var(--photo-warm), transparent 70%),
      linear-gradient(160deg, var(--photo-light) 0%, var(--photo-mid) 55%, var(--photo-light) 100%);
  }

  .cashback-tag {
    position: absolute; left: 59px; top: 1013px; width: 488px; height: 166px;
    background: var(--yellow); color: var(--ink);
    font-weight: 700; font-size: 33px; line-height: 44px; text-align: center;
    display: flex; align-items: center; justify-content: center;
  }

  .brand-corner { position: absolute; left: 0; top: 0; width: 1200px; height: 2544px; pointer-events: none; }

  .brand-name {
    position: absolute; left: 640px; top: 1104px; width: 520px;
    text-align: center; color: var(--ink);
    font-weight: 700; font-size: 54px; line-height: 60px;
  }

  .divider-line { position: absolute; left: 0; top: 1187px; width: 1200px; height: 8px; background: var(--yellow); }

  .offer-panel {
    position: absolute; left: 0; top: 1195px; width: 1200px; height: 1289px;
    color: var(--white); text-align: center;
  }
  .offer-amount { position: absolute; left: 0; width: 100%; top: 56px; font-weight: 800; font-size: 146px; line-height: 150px; }
  .offer-conditions { position: absolute; left: 0; width: 100%; top: 240px; font-weight: 700; font-size: 54px; line-height: 60px; }
  .offer-reward { position: absolute; left: 0; width: 100%; top: 352px; font-weight: 700; font-size: 72px; line-height: 98px; }
  .call-label { position: absolute; left: 0; width: 100%; top: 610px; color: var(--yellow); font-weight: 700; font-size: 94px; line-height: 112px; }
  .call-number { position: absolute; left: 0; width: 100%; top: 734px; color: var(--yellow); font-weight: 700; font-size: 100px; line-height: 116px; letter-spacing: 2px; }
  .web-address { position: absolute; left: 0; width: 100%; top: 918px; color: var(--yellow); font-weight: 700; font-size: 50px; line-height: 60px; }
  .fine-print {
    position: absolute; left: 70px; width: 1060px; top: 1066px;
    font-weight: 400; font-size: 28.5px; line-height: 35px;
  }

  .footer-band { position: absolute; left: 0; top: 2484px; width: 1200px; height: 60px; background: var(--yellow); }
</style>
</head>
<body>
  <main class="flyer">
    <header class="header-band">
      <h1 class="headline">Find the right<br>finance solution</h1>
    </header>

    <div class="hero-photo" role="img" aria-label="Photo of a hand holding a small model house with a red roof"></div>

    <svg class="brand-corner" viewBox="0 0 1200 2544" aria-hidden="true">
      <polygon points="580,1187 890,806 1200,1187" fill="#ffffff"/>
    </svg>
    <div class="brand-name">KeyHaven Finance</div>

    <p class="cashback-tag">Get up to $3000 voucher<br>or cash back* on the<br>settlement of your loan.</p>

    <div class="divider-line"></div>

    <section class="offer-panel">
      <p class="offer-amount">UP TO $3000</p>
      <p class="offer-conditions">*CONDITIONS APPLY</p>
      <p class="offer-reward">GET REWARDED BY<br>SWITCHING OVER</p>
      <p class="call-label">Call us on</p>
      <p class="call-number">0400 555 018</p>
      <p class="web-address">www.keyhavenfinance.com.au</p>
      <p class="fine-print">*based on the size of the loan, you get up to 0.3% of your total loan settled through us. For example a refinance of $600,000 mortgage to any of our panel lenders will get you $ 0.30% of the $600,000, which is $1,800 as your bonus/reward.</p>
    </section>

    <div class="footer-band"></div>
  </main>
</body>
</html>
```